Velmora Biz Card 2019

New business card for Velmora Property Inspections. We are a residential home inspection company in Arizona.

Target Market(s)

Real Estate

Font styles to use
Sans Serif

Requirements
Must have
• Glen Mirewick
• Home Inspector
• Velmora Property Inspections, LLC
• 480-555-0172
• glen@velmora-llc.example

```html
<!DOCTYPE html>
<html lang="en">
<head>
<meta charset="utf-8">
<title>Velmora Business Card</title>
<link rel="stylesheet" href="https://fonts.googleapis.com/css2?family=Montserrat:wght@400;500;800&family=Oswald:wght@700&display=swap">
<style>
  :root {
    --stage: #161616;
    --card: #222222;
    --card-edge: #2a2a2a;
    --green: #3db54a;
    --white: #f4f4f4;
  }
  * { box-sizing: border-box; margin: 0; padding: 0; }
  html, body {
    width: 1200px; height: 900px; overflow: hidden;
    background: var(--stage);
    font-family: "Montserrat", sans-serif;
  }
  .canvas {
    width: 1200px; height: 900px;
    display: flex; flex-direction: column; align-items: center; justify-content: center;
    gap: 30px;
  }
  .card {
    position: relative;
    width: 700px; height: 400px;
    background: linear-gradient(135deg, var(--card) 0%, var(--card-edge) 100%);
    border-bottom: 6px solid var(--green);
    box-shadow: 0 10px 30px rgba(0,0,0,.5);
  }
  .card-front {
    display: flex; flex-direction: column; align-items: center; justify-content: center;
  }
  .brand {
    display: flex; align-items: center; gap: 18px;
  }
  .brand-mark {
    width: 22px; height: 22px; background: var(--green); flex: none;
  }
  .brand-name {
    font-weight: 800; font-size: 34px; line-height: 1.25; letter-spacing: 2px;
    color: var(--white); text-transform: uppercase;
  }
  .identity {
    position: absolute; left: 30px; top: 128px; width: 300px;
    text-align: right;
  }
  .person-name {
    font-family: "Oswald", sans-serif; font-weight: 700;
    font-size: 42px; line-height: 1; color: var(--green);
    text-transform: uppercase; letter-spacing: .5px; white-space: nowrap;
  }
  .person-role {
    margin-top: 6px; font-size: 20px; color: var(--white);
  }
  .divider {
    position: absolute; left: 356px; top: 120px;
    width: 3px; height: 100px; background: var(--green);
  }
  .contacts {
    position: absolute; left: 386px; top: 122px;
    list-style: none; display: flex; flex-direction: column; gap: 8px;
  }
  .contacts li {
    display: flex; align-items: center; gap: 10px;
    font-size: 20px; color: var(--white); white-space: nowrap;
  }
  .icon { width: 16px; height: 16px; flex: none; }
  .address {
    position: absolute; left: 0; right: 0; bottom: 46px;
    display: flex; justify-content: center; align-items: center; gap: 10px;
    font-size: 22px; color: var(--white);
  }
</style>
</head>
<body>
<main class="canvas">
  <section class="card card-front" aria-label="Card front">
    <div class="brand">
      <span class="brand-mark"></span>
      <span class="brand-name">Velmora Property<br>Inspections, LLC</span>
    </div>
  </section>

  <section class="card card-back" aria-label="Card back">
    <div class="identity">
      <h1 class="person-name">Glen Mirewick</h1>
      <p class="person-role">Home Inspector</p>
    </div>
    <div class="divider"></div>
    <ul class="contacts">
      <li>
        <svg class="icon" viewBox="0 0 16 16" fill="none" stroke="var(--green)" stroke-width="1.6" stroke-linejoin="round"><path d="M3 1.5h3l1 3.5-2 1.3a9 9 0 0 0 4.7 4.7L11 9l3.5 1v3A1.5 1.5 0 0 1 13 14.5 11.5 11.5 0 0 1 1.5 3 1.5 1.5 0 0 1 3 1.5z"/></svg>
        480-555-0172
      </li>
      <li>
        <svg class="icon" viewBox="0 0 16 16" fill="none" stroke="var(--green)" stroke-width="1.4"><rect x="1" y="3" width="14" height="10" rx="1"/><path d="M1.5 3.5 8 9l6.5-5.5"/></svg>
        glen@velmora-llc.example
      </li>
      <li>
        <svg class="icon" viewBox="0 0 16 16" fill="none" stroke="var(--green)" stroke-width="1.3"><circle cx="8" cy="8" r="6.5"/><ellipse cx="8" cy="8" rx="3" ry="6.5"/><path d="M1.5 8h13M2.5 4.8h11M2.5 11.2h11"/></svg>
        www.velmora-llc.example
      </li>
    </ul>
    <p class="address">
      <svg class="icon" viewBox="0 0 16 16" fill="var(--green)"><path d="M8 1 0.5 8h2v7h4.5v-4.5h2V15h4.5V8h2z"/></svg>
      Corvale, AZ 85990, USA
    </p>
  </section>
</main>
</body>
</html>
```